Square Business Cards for Our Restaurant / Event Venue

We need square business cards designed for the management team of our event venue and restaurant. On one side of the card should be the the Harbor Lantern 7 logo and URL www.harborlantern7.example. On the other side should be the Ember Logo and URL www.emberhall7.example. All employee details should be on the side with Ember logo. There will be a total of 5 cards to be created with the design.

Clara Bennquist
clara@harborlantern7.example

main 555.418.3072
direct 555.730.2946

4831 West Orchard Lane SE
Washington, DC 90417

Industry/Entity Type

Business

```html
<!DOCTYPE html>
<html lang="en">
<head>
<meta charset="utf-8">
<title>Harbor Lantern 7 — Square Business Cards</title>
<link href="https://fonts.googleapis.com/css2?family=Encode+Sans+Semi+Condensed:wght@400;600;700&display=swap" rel="stylesheet">
<style>
  :root {
    --backdrop: #e4e6e5;
    --card: #ffffff;
    --brand-red: #b21f24;
    --ink: #15172a;
    --bar-black: #111111;
    --text-dark: #222222;
    --pattern-red-soft: #f1d3d4;
    --pattern-grey-soft: #e2e2e2;
  }
  * { box-sizing: border-box; margin: 0; padding: 0; }
  html, body {
    width: 1200px; height: 900px; overflow: hidden;
    background: var(--backdrop);
  }
  .sheet { position: relative; width: 1200px; height: 900px; }
  .card {
    position: absolute; top: 230px;
    width: 440px; height: 440px;
    background: var(--card);
    box-shadow: 0 6px 18px rgba(0,0,0,0.18);
    overflow: hidden;
    font-family: "Encode Sans Semi Condensed", sans-serif;
  }
  .card--front { left: 130px; }
  .card--back { left: 630px; }

  /* Front */
  .front__pattern {
    position: absolute; left: 0; bottom: 0; width: 160px; height: 200px;
    background: linear-gradient(45deg, var(--pattern-red-soft), rgba(255,255,255,0) 75%);
  }
  .front__brand {
    position: absolute; left: 0; right: 0; top: 160px;
    display: flex; align-items: center; justify-content: center; gap: 14px;
  }
  .front__mark {
    width: 30px; height: 30px; border-radius: 50%;
    background: var(--brand-red); flex: none;
  }
  .front__name {
    font-weight: 600; color: var(--brand-red);
    font-size: 38px; line-height: 1;
  }
  .front__url-bar {
    position: absolute; right: 0; bottom: 14px;
    width: 275px; height: 36px; background: var(--bar-black);
    display: flex; align-items: center; justify-content: center;
  }
  .front__url { color: #fff; font-size: 16px; letter-spacing: 0.2px; }

  /* Back */
  .back__pattern {
    position: absolute; right: 0; top: 0; width: 200px; height: 180px;
    background: linear-gradient(225deg, var(--pattern-grey-soft), rgba(255,255,255,0) 75%);
  }
  .back__brand {
    position: absolute; left: 62px; top: 84px;
    display: flex; align-items: center; gap: 12px;
  }
  .back__mark {
    width: 18px; height: 18px; border-radius: 50%;
    background: var(--brand-red); flex: none;
  }
  .back__name-text {
    font-weight: 700; color: var(--ink);
    font-size: 60px; line-height: 1;
  }
  .back__url {
    position: absolute; left: 62px; top: 168px;
    font-weight: 600; color: var(--text-dark); font-size: 15px;
  }
  .back__name-band {
    position: absolute; left: 112px; right: 0; top: 192px; height: 34px;
    background: var(--brand-red);
    display: flex; align-items: center; padding-left: 16px;
  }
  .back__name { font-weight: 700; color: #fff; font-size: 23px; letter-spacing: 0.3px; }
  .contact {
    position: absolute; left: 100px; top: 262px;
    list-style: none;
    color: var(--text-dark); font-size: 14px; letter-spacing: 1px;
  }
  .contact__row { display: flex; align-items: flex-start; gap: 10px; margin-bottom: 6px; }
  .contact__icon { flex: none; width: 14px; height: 14px; margin-top: 2px; }
  .contact__label { font-size: 11px; margin-right: 4px; }
  .contact__text { line-height: 1.35; }
</style>
</head>
<body>
<main class="sheet">

  <section class="card card--front" aria-label="Card front">
    <div class="front__pattern" role="img" aria-label="Decorative red dot pattern area"></div>
    <div class="front__brand">
      <span class="front__mark" aria-hidden="true"></span>
      <p class="front__name">Harbor Lantern 7</p>
    </div>
    <div class="front__url-bar"><span class="front__url">www.harborlantern7.example</span></div>
  </section>

  <section class="card card--back" aria-label="Card back">
    <div class="back__pattern" role="img" aria-label="Decorative black dot pattern area"></div>
    <div class="back__brand">
      <span class="back__mark" aria-hidden="true"></span>
      <p class="back__name-text">Ember</p>
    </div>
    <p class="back__url">www.emberhall7.example</p>
    <div class="back__name-band"><span class="back__name">Clara Bennquist</span></div>

    <ul class="contact">
      <li class="contact__row">
        <svg class="contact__icon" viewBox="0 0 16 16" aria-hidden="true">
          <circle cx="8" cy="8" r="8" fill="var(--brand-red)"/>
          <rect x="4" y="5" width="8" height="6" fill="none" stroke="#fff" stroke-width="1"/>
          <path d="M4 5 L8 8.5 L12 5" fill="none" stroke="#fff" stroke-width="1"/>
        </svg>
        <span class="contact__text">clara@harborlantern7.example</span>
      </li>
      <li class="contact__row">
        <svg class="contact__icon" viewBox="0 0 16 16" aria-hidden="true">
          <circle cx="8" cy="8" r="8" fill="var(--brand-red)"/>
          <rect x="5.5" y="3.5" width="5" height="9" rx="1" fill="none" stroke="#fff" stroke-width="1"/>
        </svg>
        <span class="contact__text"><span class="contact__label">main</span>555.418.3072</span>
      </li>
      <li class="contact__row">
        <svg class="contact__icon" viewBox="0 0 16 16" aria-hidden="true">
          <circle cx="8" cy="8" r="8" fill="var(--brand-red)"/>
          <rect x="5.5" y="3.5" width="5" height="9" rx="1" fill="none" stroke="#fff" stroke-width="1"/>
        </svg>
        <span class="contact__text"><span class="contact__label">direct</span>555.730.2946</span>
      </li>
      <li class="contact__row">
        <svg class="contact__icon" viewBox="0 0 16 16" aria-hidden="true">
          <circle cx="8" cy="8" r="8" fill="var(--brand-red)"/>
          <path d="M8 13 C5.5 9.5 5 8.3 5 7 A3 3 0 0 1 11 7 C11 8.3 10.5 9.5 8 13 Z" fill="#fff"/>
          <circle cx="8" cy="7" r="1" fill="var(--brand-red)"/>
        </svg>
        <span class="contact__text">4831 West Orchard Lane SE<br>Washington, DC 90417</span>
      </li>
    </ul>
  </section>

</main>
</body>
</html>
```